We need a completed book cover (front and back) for a Christian devotional book titled "Walking Steady Onward: Shaped as an Open PATH Follower" by Dr. Martin Hale. The publishing company should be "Open Path" (https://opnpathhub.org). This will be for small groups to go through together daily to understand how to grow as a Christian as a part of the family of God. I'm attaching the Open Path logo and the introduction to the book.
Main themes include navigating today’s culture, understanding and using our spiritual gifts, and experiencing joy in community.

```html
<!DOCTYPE html>
<html lang="en">
<head>
<meta charset="utf-8">
<title>Walking Steady Onward – Cover Spread</title>
<link rel="stylesheet" href="https://fonts.googleapis.com/css2?family=Montserrat:wght@800&family=Open+Sans:wght@400;600;700&display=swap">
<style>
  :root {
    --page-bg: #e7e3dd;
    --sky-dark: #3f3a35;
    --sky-mid: #8a7f72;
    --sky-light: #d9cfbf;
    --haze: #b8ad9d;
    --crowd: #1c1916;
    --title-red: #a3173b;
    --ink-dark: #26221e;
    --ink-light: #f6f2ec;
  }
  * { margin: 0; padding: 0; box-sizing: border-box; }
  html, body { width: 1200px; height: 800px; overflow: hidden; }
  body {
    background: var(--page-bg);
    font-family: "Open Sans", Arial, sans-serif;
    position: relative;
  }
  .cover-spread {
    position: absolute;
    left: 96px; top: 40px;
    width: 1008px; height: 720px;
    display: flex;
    box-shadow: 0 6px 24px rgba(0,0,0,.25);
  }
  .panel { position: relative; height: 100%; overflow: hidden; }
  .back-cover { width: 480px; }
  .spine { width: 48px; }
  .front-cover { width: 480px; }

  .scene-art {
    position: absolute; inset: 0;
    background:
      radial-gradient(ellipse 70% 30% at 55% 45%, rgba(235,226,210,.75), transparent 70%),
      linear-gradient(to bottom, var(--sky-dark) 0%, var(--sky-mid) 18%, var(--sky-light) 42%, var(--haze) 58%, #5a524a 72%, var(--crowd) 100%);
  }
  .back-cover .scene-art {
    background:
      radial-gradient(ellipse 60% 25% at 30% 40%, rgba(220,210,195,.6), transparent 70%),
      linear-gradient(to bottom, #2e2a27 0%, #5b534b 20%, #a99d8d 42%, #9a8f80 58%, #4a433c 72%, var(--crowd) 100%);
  }
  .spine .scene-art {
    background: linear-gradient(to bottom, #6c6258 0%, #cfc5b5 30%, #d7cdbd 55%, #8c8174 78%, #2a2622 100%);
  }

  /* Front */
  .front-title {
    position: absolute; left: 58px; top: 150px;
    font-family: "Montserrat", Arial, sans-serif;
    font-weight: 800;
    font-size: 62px;
    line-height: 1.0;
    letter-spacing: -0.5px;
    color: var(--title-red);
    text-transform: uppercase;
  }
  .front-subtitle {
    position: absolute; left: 60px; top: 355px;
    font-size: 15.5px;
    letter-spacing: 1.5px;
    color: var(--ink-dark);
    text-transform: uppercase;
  }
  .front-author {
    position: absolute; right: 60px; top: 630px;
    font-weight: 700;
    font-size: 22px;
    letter-spacing: 2px;
    color: var(--ink-light);
    text-transform: uppercase;
  }

  /* Spine */
  .spine-text {
    position: absolute; left: 50%; top: 26px;
    transform: translateX(-50%);
    writing-mode: vertical-rl;
    font-size: 12.5px;
    color: var(--ink-dark);
    text-transform: uppercase;
    letter-spacing: .5px;
    white-space: nowrap;
  }
  .spine-title strong { font-weight: 700; }
  .spine-author {
    position: absolute; left: 50%; bottom: 40px;
    transform: translateX(-50%);
    writing-mode: vertical-rl;
    font-weight: 700;
    font-size: 13px;
    letter-spacing: 1.5px;
    color: var(--ink-dark);
    text-transform: uppercase;
    white-space: nowrap;
  }

  /* Back */
  .back-content {
    position: absolute; left: 52px; right: 52px; top: 70px;
    color: var(--ink-light);
    text-align: center;
  }
  .back-title {
    font-weight: 700;
    font-size: 15px;
    text-transform: uppercase;
    letter-spacing: .3px;
  }
  .back-subtitle {
    font-size: 14px;
    text-transform: uppercase;
    margin-bottom: 18px;
  }
  .back-body p {
    font-size: 10.5px;
    line-height: 1.5;
    margin-bottom: 10px;
  }
  .back-story {
    position: absolute; left: 52px; right: 52px; top: 520px;
    color: var(--ink-light);
    text-align: center;
    font-size: 10.5px;
    line-height: 1.5;
  }
</style>
</head>
<body>
  <main class="cover-spread">
    <section class="panel back-cover">
      <div class="scene-art" role="img" aria-label="Cloudy sepia sky above a vast dark crowd"></div>
      <div class="back-content">
        <h2 class="back-title">Walking Steady Onward</h2>
        <p class="back-subtitle">Shaped as an Open PATH Follower</p>
        <div class="back-body">
          <p>Inviting Jesus to live in your daily life is the most fulfilling opportunity you may ever take on. If you are someone re-committing your life to Him after a season away, and you are serious this time, you may be surprised with what He has in store for you in these pages. Either way, discovering God's purposes for your day-to-day life will find great fulfillment in the pages of Walking Steady Onward. You have the chance to discover a new level of personal growth as you know Him more and more. You also will understand that He has prepared a life-giving community around you, the place He brings change in every one of our lives. Yes, moving onto the Open PATH as you grow in Christ will take you on a most unusual adventure. In fact, we hope that you actually go through this devotional with two or three others to bring the Open PATH realities home immediately in your life.</p>
          <p>As you take the initial steps into this devotional, consider these three approaches to using this daily guide to following Jesus with others He has brought alongside.</p>
        </div>
      </div>
      <p class="back-story">Joel Kirunda and I have partnered together in east Africa for close to 20 years, and we love to take a concept and go deeper together on how we communicate that principle to young leaders. I brought the idea of Watch, Wait, and Listen to Joel: let's give people a simple means to think more deeply about the biblical principles by using these three action words. Joel, ever so gracious, responded simply, "This is a wonderful approach to helping people go deeper. May I suggest, at least for Americans, that you add one more word at the beginning." My friend, ever so gentle in his demeanor, suddenly yelled out the word:</p>
    </section>

    <section class="panel spine">
      <div class="scene-art" role="img" aria-label="Pale sky with birds fading into crowd"></div>
      <p class="spine-text"><span class="spine-title"><strong>Walking Steady Onward:</strong> Shaped as an Open PATH Follower</span></p>
      <p class="spine-author">Dr. Martin Hale</p>
    </section>

    <section class="panel front-cover">
      <div class="scene-art" role="img" aria-label="Hooded figure seen from behind facing a great crowd under a bright cloudy sky"></div>
      <h1 class="front-title">Walking<br>Steady<br>Onward</h1>
      <p class="front-subtitle">Shaped as an Open PATH Follower</p>
      <p class="front-author">Dr. Martin Hale</p>
    </section>
  </main>
</body>
</html>
```